Edible Insect Sticker packaging design

The successful designer for this product will be hired again for more packaging design products in this product range.
We are a company that manufactures edible insects and we have some new products coming out we ned packaging for. As you can imagine the stickers are very small 50mm x 50mm.
Each sticker design will be in a set  of 2 (one for the front and one for the back of the packaging).
The front will contain the weight of the product (in grams) as well as the name of the product and design.
The back will contain our company logo and info as well as NIP (Nutritional Information Panel), ingredient declaration, and 3-4 lines of information about how edible insects are great for the environment.
At this stage I would like the packaging to have a slightly environmental free, but still colourful and eye catching. I am open to any suggestions for the design though if you have some great ideas!
Must also contain the slogan (on front or back), "Are you Brave Enough?"
There are several products in the range, and would like the labels to be in a set. Basic lay out will be the same for each product, and the front sticker will be slightly different.
Products are
Zib-A-Lop Tundle- a fly shaped chocolate that contains coconut and fly pupae
Plinky Pebbles- 5 x roasted crickets
Tootle Twirlies- 5 x roasted mealworms
Fudge Dipped Fidgets- 5 x insects, chocolate coated in milk, white or dark chocolate. Insects include crickets, mealworms and fly pupae
Specific information (eg, NIP, ingredients etc) will be sent to chosen designer to add to the deisgn.
Attached is image of 3 products (Zib-A-Lop Tundle, roasted mealworms and roasted crickets) as well as logo. The chocolate coated bugs are the 2 types of roasted bugs pictured in the attachment coated in chocolate.

Updates
Design can be square or round 

Reason: Several designers have asked for an extension to submit new/ revised designs.

Reason: I have extended the deadline by one day to allow for revisions and new designs to be submitted.

```html
<!DOCTYPE html>
<html lang="en">
<head>
<meta charset="utf-8">
<title>Plinky Pebbles – Front Label</title>
<link rel="stylesheet" href="https://fonts.googleapis.com/css2?family=Lilita+One&family=Alfa+Slab+One&display=swap">
<style>
  :root {
    --stripe-light: #a87b3e;
    --stripe-dark: #9a6d33;
    --band-edge: #7d5426;
    --band-center: #ecd29a;
    --band-side: #c99e5e;
    --red: #d4202b;
    --white: #ffffff;
    --ink-shadow: #3b2410;
  }
  * { margin: 0; padding: 0; box-sizing: border-box; }
  html, body { width: 1200px; height: 1200px; overflow: hidden; }
  body { background: var(--stripe-light); }

  .label {
    position: relative;
    width: 1200px;
    height: 1200px;
    overflow: hidden;
    background: repeating-linear-gradient(
      to bottom,
      var(--stripe-light) 0 38px,
      var(--stripe-dark) 38px 76px
    );
  }

  .center-band {
    position: absolute;
    left: 335px;
    top: 0;
    width: 540px;
    height: 1200px;
    background: var(--band-edge);
    padding: 0 30px;
  }
  .center-band__inner {
    width: 100%;
    height: 100%;
    background: radial-gradient(ellipse at 50% 40%, var(--band-center) 0%, #dcb97c 45%, var(--band-side) 100%);
  }

  .insect-art {
    position: absolute;
    left: 480px;
    top: 430px;
    width: 260px;
    height: 750px;
    border-radius: 120px 120px 60px 60px;
    background: radial-gradient(ellipse at 50% 40%, rgba(140, 95, 55, 0.45), rgba(140, 95, 55, 0.12) 70%, transparent 100%);
  }

  .product-name {
    position: absolute;
    left: 0;
    top: 80px;
    width: 1200px;
    text-align: center;
    font-family: "Lilita One", system-ui, sans-serif;
    font-weight: 400;
    font-size: 160px;
    line-height: 1;
    color: var(--white);
  }
  .product-name span { display: block; }

  .count {
    position: absolute;
    left: 40px;
    top: 720px;
    width: 430px;
    text-align: center;
    font-family: "Lilita One", system-ui, sans-serif;
    color: var(--white);
    line-height: 0.95;
    text-shadow: 6px 6px 0 var(--ink-shadow);
  }
  .count__number { font-size: 130px; display: block; }
  .count__words { font-size: 72px; display: block; }

  .weight {
    position: absolute;
    right: 70px;
    top: 730px;
    font-family: "Alfa Slab One", Georgia, serif;
    font-size: 128px;
    color: var(--white);
    text-shadow: 6px 6px 0 var(--ink-shadow);
  }

  .slogan {
    position: absolute;
    left: -60px;
    top: 1030px;
    width: 1320px;
    height: 104px;
    background: var(--red);
    transform: rotate(-3.6deg);
    box-shadow: 0 8px 0 rgba(60, 10, 10, 0.35);
    display: flex;
    align-items: center;
    justify-content: center;
    gap: 34px;
  }
  .slogan__text {
    font-family: "Lilita One", system-ui, sans-serif;
    font-size: 64px;
    color: var(--white);
    letter-spacing: 2px;
    white-space: nowrap;
  }
  .slogan__arrow { width: 38px; height: 42px; fill: var(--white); }
</style>
</head>
<body>
  <main class="label">
    <div class="center-band"><div class="center-band__inner"></div></div>

    <div class="insect-art" role="img" aria-label="Engraved-style illustration of a roasted cricket, seen from above"></div>

    <h1 class="product-name"><span>PLINKY</span><span>PEBBLES</span></h1>

    <p class="count">
      <span class="count__number">5X</span>
      <span class="count__words">ROASTED</span>
      <span class="count__words">CRICKETS</span>
    </p>

    <p class="weight">30g</p>

    <div class="slogan">
      <svg class="slogan__arrow" viewBox="0 0 38 42"><polygon points="0,0 38,21 0,42"/></svg>
      <span class="slogan__text">ARE YOU BRAVE ENOUGH?</span>
      <svg class="slogan__arrow" viewBox="0 0 38 42"><polygon points="38,0 0,21 38,42"/></svg>
    </div>
  </main>
</body>
</html>
```